Business card design needed

Front of Card:
I would like to have nearly 3/4 of the card from the top in a Pea Green Colour with the word 'Lanternfield' written in a(Watermelon Red colour) in the font 'Viner Hand ITC'. Lanternfield to be written within the Green colour of the card.

The lower 1/3 of the card I would like to have white with the words:
Home and Garden Styling smaller than the word Lanternfield in Black in the font 'Batang', centred underneath the green section.

At the very bottom in one corner in smaller print I would like to have my contact phone number: Pip M:0437960214 and then the email address:
E: lanternfieldstyling@quobnet.net.au on the other side.

Back of Card:
Back of Card to be White
On one side (Left)
I would like the Heading "Garden" in the same pea green colour as the front and in the Viner Hand ITC font. On the other half of the card I would like 'Home' in the Watermelon Red Colour (same as front colour) and in the font Viner Hand ITC.
Underneath these Headings I would like written in black and in Batang font the following list of services.

Garden Home
Garden Styling Interior Styling
Plant Selection Furniture Selection/Arrangement Garden Maintenance Setting Up Home (after move)
Hedging/Mowing Merchandise and Stylist for
Work w/Local Nurseries Brenna and Hask

Lanternfield
Home and Garden Styling
M: 0437960214 E: lanternfieldstyling@quobnet.net.au

```html
<!DOCTYPE html>
<html lang="en">
<head>
<meta charset="utf-8">
<title>Lanternfield business card</title>
<link rel="stylesheet" href="https://fonts.googleapis.com/css2?family=Caveat+Brush&family=Gelasio:wght@400&display=swap">
<style>
  :root {
    --pea-green: #9bcc3e;
    --pea-green-light: #aad651;
    --watermelon: #d23a4f;
    --ink: #1c1c1c;
    --paper: #ffffff;
    --paper-tint: #f1f1f1;
    --backdrop: #e6e6e4;
    --script: "Caveat Brush", cursive;
    --serif: "Gelasio", serif;
  }
  html, body {
    margin: 0;
    width: 1200px;
    height: 900px;
    overflow: hidden;
    background: var(--backdrop);
  }
  .sheet {
    position: relative;
    width: 1200px;
    height: 900px;
    display: flex;
    align-items: center;
    justify-content: center;
    gap: 50px;
  }
  .card {
    position: relative;
    width: 525px;
    height: 300px;
    background: var(--paper);
    box-shadow: 0 6px 18px rgba(0,0,0,0.18);
    overflow: hidden;
  }

  /* Back of card */
  .card-back__pattern {
    position: absolute;
    inset: 0;
    background: radial-gradient(circle at 40% 50%, var(--paper) 0%, var(--paper-tint) 100%);
  }
  .card-back__heading {
    position: absolute;
    margin: 0;
    font-family: var(--script);
    font-weight: 400;
    font-size: 64px;
    line-height: 1;
  }
  .card-back__heading--garden { left: 48px; top: 18px; color: var(--pea-green); }
  .card-back__heading--home { right: 40px; top: 70px; color: var(--watermelon); }
  .services {
    position: absolute;
    left: 0;
    right: 0;
    top: 150px;
    margin: 0;
    padding: 0;
    list-style: none;
    text-align: center;
    font-family: var(--serif);
    font-size: 12px;
    line-height: 1.45;
    color: var(--ink);
  }

  /* Front of card */
  .card-front__field {
    position: absolute;
    left: 0;
    top: 0;
    width: 100%;
    height: 210px;
    background: linear-gradient(135deg, var(--pea-green-light), var(--pea-green));
  }
  .card-front__name {
    position: absolute;
    left: 0;
    right: 0;
    top: 58px;
    margin: 0;
    text-align: center;
    font-family: var(--script);
    font-weight: 400;
    font-size: 84px;
    line-height: 1;
    color: var(--watermelon);
  }
  .card-front__tagline {
    position: absolute;
    left: 0;
    right: 0;
    top: 222px;
    margin: 0;
    text-align: center;
    font-family: var(--serif);
    font-size: 22px;
    color: var(--ink);
  }
  .contact {
    position: absolute;
    bottom: 12px;
    display: flex;
    align-items: center;
    gap: 5px;
    font-family: var(--serif);
    font-size: 10px;
    color: var(--ink);
  }
  .contact--email { left: 14px; }
  .contact--phone { right: 14px; }
  .contact svg { width: 11px; height: 11px; }
</style>
</head>
<body>
<main class="sheet">
  <section class="card card-back" aria-label="Back of card">
    <div class="card-back__pattern" role="img" aria-label="Faint grey floral scroll pattern"></div>
    <h2 class="card-back__heading card-back__heading--garden">Garden</h2>
    <h2 class="card-back__heading card-back__heading--home">Home</h2>
    <ul class="services">
      <li>Garden Home</li>
      <li>Garden Styling Interior Styling</li>
      <li>Plant Selection Furniture Selection/Arrangement Garden Maintenance Setting Up</li>
      <li>Home (after move)</li>
      <li>Hedging/Mowing Merchandise and Stylist for</li>
      <li>Work/Local Nurseries Brenna and Hask</li>
    </ul>
  </section>

  <section class="card card-front" aria-label="Front of card">
    <div class="card-front__field" role="img" aria-label="Pea green panel with light green leaf scroll pattern"></div>
    <h1 class="card-front__name">Lanternfield</h1>
    <p class="card-front__tagline">Home and Garden Styling</p>
    <p class="contact contact--email">
      <svg viewBox="0 0 12 12" aria-hidden="true"><rect x="0.75" y="2.25" width="10.5" height="7.5" fill="none" stroke="#1c1c1c" stroke-width="1"/><path d="M0.75 2.25 L6 6.5 L11.25 2.25" fill="none" stroke="#1c1c1c" stroke-width="1"/></svg>
      lanternfieldstyling@quobnet.net.au
    </p>
    <p class="contact contact--phone">
      <svg viewBox="0 0 12 12" aria-hidden="true"><path d="M3 1 L5 3.5 L4 5 Q5 7 7 8 L8.5 7 L11 9 L9.5 11 Q5 11 2.5 7.5 Q1 5 1.5 2.5 Z" fill="#1c1c1c"/></svg>
      Pip M:0437960214
    </p>
  </section>
</main>
</body>
</html>
```